CV for an Urgent Care Trade Association Executive search candidate in need of competitive CV refresh

I need a CV refresh to be able to show marketability and skill in a competitive Executive search. I would like to see designs that highlight my skill and ability to hopefully put me in the front running for position.

Industry/Entity Type

Medical/Urgent Care

Requirements
Must have
• CV template
Nice to have
• Nice to have a CV template to be able to add my personal info into

```html
<!DOCTYPE html>
<html lang="en">
<head>
<meta charset="utf-8">
<title>CV – Trade Association Executive</title>
<link href="https://fonts.googleapis.com/css2?family=Josefin+Sans:wght@300;400;500;600;700&display=swap" rel="stylesheet">
<style>
  :root {
    --ink: #414141;
    --band-top: #bfe4f9;
    --band-left: #d8eefb;
    --band-right: #e3f2fc;
    --shard: #d3eaf9;
    --paper: #ffffff;
  }
  * { margin: 0; padding: 0; box-sizing: border-box; }
  html, body { width: 848px; height: 1200px; overflow: hidden; background: var(--paper); }
  .cv {
    position: relative; width: 848px; height: 1200px; overflow: hidden;
    font-family: "Josefin Sans", sans-serif; color: var(--ink);
  }
  .backdrop { position: absolute; inset: 0; }
  .abs { position: absolute; white-space: nowrap; line-height: 1; }

  .name { left: 60px; top: 72px; font-size: 54px; font-weight: 400; letter-spacing: 1px; }
  .name strong { font-weight: 700; }
  .role { left: 60px; top: 128px; font-size: 26px; font-weight: 500; letter-spacing: 1px; }

  .heading { font-weight: 700; letter-spacing: 1px; }
  .heading-side { font-size: 26px; }
  .heading-main { font-size: 34px; }
  .heading-mid { font-size: 27px; }
  .rule { position: absolute; height: 2px; background: var(--ink); }

  .contact-item { left: 69px; font-size: 17px; letter-spacing: 0.8px; }
  .contact-icon { position: absolute; left: 40px; width: 16px; height: 16px; }

  .summary {
    position: absolute; left: 275px; top: 293px; width: 516px;
    font-size: 15px; line-height: 18.8px; letter-spacing: 0.9px; text-align: justify;
  }

  .skills { position: absolute; left: 0; top: 0; list-style: none; }
  .skills li, .bullets li { position: absolute; white-space: nowrap; line-height: 1; }
  .skills li { left: 54px; font-size: 17px; letter-spacing: 0.6px; }
  .skills li::before, .bullets li::before {
    content: ""; position: absolute; width: 4px; height: 4px; border-radius: 50%; background: var(--ink); top: 5px;
  }
  .skills li::before { left: -13px; }
  .skills .wrap { line-height: 16px; }

  .job-title { left: 275px; font-size: 19px; font-weight: 700; letter-spacing: 1px; }
  .company { left: 275px; font-size: 21px; font-weight: 400; letter-spacing: 1px; }
  .bullets { list-style: none; }
  .bullets li { left: 301px; font-size: 15.5px; letter-spacing: 0.8px; }
  .bullets li::before { left: -18px; }
  .bullets .wrap { line-height: 19px; }
</style>
</head>
<body>
<main class="cv">
  <svg class="backdrop" width="848" height="1200" viewBox="0 0 848 1200" aria-hidden="true">
    <polygon points="0,0 848,0 848,155 0,232" fill="var(--band-top)"/>
    <polygon points="0,387 242,434 242,904 0,857" fill="var(--band-left)"/>
    <polygon points="242,434 848,372 848,854 242,904" fill="var(--band-right)"/>
    <polygon points="682,485 797,492 678,657" fill="var(--shard)"/>
    <polygon points="817,586 828,692 710,664" fill="var(--shard)"/>
    <polygon points="670,702 797,747 722,798" fill="var(--shard)"/>
    <polygon points="0,1176 848,1096 848,1200 0,1200" fill="var(--band-top)"/>
    <circle cx="681" cy="150" r="123" fill="var(--paper)"/>
    <circle cx="681" cy="150" r="107" fill="var(--paper)" stroke="var(--ink)" stroke-width="10"/>
    <line x1="242" y1="251" x2="242" y2="1122" stroke="var(--ink)" stroke-width="2"/>
  </svg>

  <header>
    <h1 class="abs name">YOUR <strong>NAME</strong></h1>
    <p class="abs role">Trade Association Executive</p>
  </header>

  <section class="contact">
    <h2 class="abs heading heading-side" style="left:35px;top:253px">Contact</h2>
    <div class="rule" style="left:35px;top:284px;width:142px"></div>
    <svg class="contact-icon" style="top:296px" viewBox="0 0 16 16" aria-hidden="true">
      <path d="M8 1a4.5 4.5 0 0 0-4.5 4.5C3.5 9 8 12 8 12s4.5-3 4.5-6.5A4.5 4.5 0 0 0 8 1zm0 6.2a1.7 1.7 0 1 1 0-3.4 1.7 1.7 0 0 1 0 3.4z" fill="var(--ink)"/>
      <path d="M3 12.5c1 .9 3 1.5 5 1.5s4-.6 5-1.5" fill="none" stroke="var(--ink)" stroke-width="1.6"/>
    </svg>
    <p class="abs contact-item" style="top:297px">Your Location</p>
    <svg class="contact-icon" style="top:326px" viewBox="0 0 16 16" aria-hidden="true">
      <circle cx="8" cy="8" r="7.5" fill="var(--ink)"/>
      <path d="M5.2 4.3l1.3-.3.8 1.9-.9.7c.5 1.1 1.3 1.9 2.4 2.4l.7-.9 1.9.8-.3 1.3c-3.5.2-6.1-2.4-5.9-5.9z" fill="var(--paper)"/>
    </svg>
    <p class="abs contact-item" style="top:326px">Your Phone No.</p>
    <svg class="contact-icon" style="top:353px" viewBox="0 0 16 16" aria-hidden="true">
      <path d="M1 6.5 8 1l7 5.5V15H1z" fill="var(--ink)"/>
      <path d="M1.5 7 8 11l6.5-4" fill="none" stroke="var(--paper)" stroke-width="1.3"/>
    </svg>
    <p class="abs contact-item" style="top:353px">Your email</p>
  </section>

  <section class="skills-block">
    <h2 class="abs heading heading-side" style="left:35px;top:450px">Skills</h2>
    <div class="rule" style="left:35px;top:480px;width:88px"></div>
    <ul class="skills">
      <li style="top:493px">Executive search</li>
      <li style="top:518px">Talent acquisition</li>
      <li class="wrap" style="top:542px">Sourcing and<br>creening candidates</li>
      <li style="top:584px">Interviewing</li>
      <li style="top:609px">Negotiating offerst</li>
      <li style="top:635px">Relationship building</li>
      <li style="top:658px">Presentation skills</li>
      <li style="top:682px">Report writing</li>
    </ul>
  </section>

  <section class="summary-block">
    <h2 class="abs heading heading-main" style="left:275px;top:247px">Summary</h2>
    <div class="rule" style="left:275px;top:284px;width:199px"></div>
    <p class="summary">Seasoned executive search consultant with over 15 years of experience in the technology industry. Proven track record of successfully identifying and placing top talent at leading companies. Expertise in all aspects of the executive search process, from sourcing and screening candidates to negotiating offers.</p>
  </section>

  <section class="experience">
    <h2 class="abs heading heading-main" style="left:275px;top:451px">Experience</h2>
    <div class="rule" style="left:275px;top:489px;width:217px"></div>

    <h3 class="abs job-title" style="top:500px">Executive Search Consultant</h3>
    <p class="abs company" style="top:528px">ABC Executive Search</p>
    <ul class="bullets">
      <li class="wrap" style="top:563px">Managed the full executive search process for a<br>variety of technology companies</li>
      <li style="top:608px">Sourced and screened hundreds of candidates</li>
      <li style="top:633px">Conducted dozens of interviews</li>
      <li style="top:658px">Negotiated and closed dozens of offers</li>
    </ul>

    <h3 class="abs job-title" style="top:696px">Senior Executive Recruiter</h3>
    <p class="abs company" style="top:724px">XYZ Executive Search</p>
    <ul class="bullets">
      <li style="top:760px">Led a team of executive recruiters</li>
      <li style="top:785px">Managed a portfolio of clients</li>
      <li style="top:811px">Developed and implemented recruiting strategies</li>
      <li style="top:838px">Recruited and placed top talent at leading companies</li>
    </ul>
  </section>

  <section class="education">
    <h2 class="abs heading heading-mid" style="left:275px;top:914px">Education</h2>
    <div class="rule" style="left:275px;top:942px;width:160px"></div>
    <ul class="bullets">
      <li style="top:959px">MBA, Westbrook University</li>
      <li style="top:983px">BS, Computer Science, Harbor State University</li>
    </ul>
  </section>

  <section class="awards">
    <h2 class="abs heading heading-mid" style="left:275px;top:1017px">Awards and Honors</h2>
    <div class="rule" style="left:275px;top:1045px;width:270px"></div>
    <ul class="bullets">
      <li style="top:1060px">Trade Association Executive of the Year, ABC Trade Association</li>
      <li style="top:1084px">President's Award, XYZ Trade Association</li>
    </ul>
  </section>
</main>
</body>
</html>
```